Football (soccer) board game app design

Hi,

We are a start up looking for a gameplay design for an app. It is a football trivia app that consists of four main screens; login/register, main navigation, gameplay, question.

OVERALL:
We want our app to be kept in a dark theme. Black or very dark gray is preferable, with a couple of nice colors to give it a stylish touch. We like flat designs, but are open for ideas within the general structure design. The logo can be used in the app, but feel free to improve it you feel you can. In the attached material we have tried to outline some of our ideas and other designs friends have helped us make.

LOGIN/REGISTER:
We want a simple login. Email, password, Chatterly login and the possibility to register a new user. Live search check whether the email is valid and free, and there is also live validation of passwords. If this could be incorporated in the design it would be nice.

MAIN NAVIGATION:
In the main navigation screen we want it to be divided into tabs. A home, my games, my categories and a ranking tab. In the top bar it should be possible to search for categories as well as there should be a button to go to settings.

The Home tab
In the home tab we want a "Quick Play" button, and a list of featured categories. A category can be unlocked or locked, which should be illustrated somehow. When a category is tapped it should divide the block into a left and right tap area, where the user can choose to "Beat to unlock" or "Buy to unlock" if locked and "Practice" or "Challenge Friend" if already unlocked.

The My Games tab
In the my games tab, the current games should be divided into three lists. First "your turn", then "opponents turn" and finally "finished games".

The My Categories tab
This tab should include a list of categories, which the user have bought, but as of design it is fairly similar to the blocks in home tab. So not much different here.

The Ranking tab
Ranking should show a set of leaderboards; Today, This Week, This Month, etc. The row in a leaderboard should have teamname and a win percentage.

GAMEPLAY:
The gameplay is inspired by an old football (soccer) board game from the 1950's, and our gameplay consists of three core elements; a football (soccer) pitch, 11 players and a scoreboard.

The football (soccer) pitch
What we need is a pitch seen from behind the goal line. The important issue here, is the perspective, as we want 11 players on the field formed as a 4-3-3 formation, being 1 goalkeeper, 4 defenders, 3 midfielder and 3 strikers. They should all be touchable without overlap. In the other end we want a goal that should be touchable as well. The goal in the nearest end do not have to be visible. Due to the perspective of the field and the fact that players and goal should be touchable, of course give you the opportunity to play around with the proportions of both players and goal. We rather want a large goal being out of proportions, than a small goal with a tiny tap area. Around the field (sidelines and beside the goal) we would like advertising banners like seen on a real stadium.

The players
As mentioned we want 11 players in a 4-3-3 formation. The players should be attached to the board with springs as seen on some of the very old board games, where you could flick the player to pass the ball. This also means that we want the players to be placed in an indentation for the ball to fall into and it would be very cool if you could illustrate the player with the ball, as being pulled back to one of the sides, just enough to see the ball at his feet. The players should be large enough for a user to tap them, hence it would also be beneficial if they are not overlapping. For a start we would like to see the players in a blue shirt and white shorts (socks are not necessary as they are placed on a spring).

Scoreboard
On the scoreboard above the field, we need information such as the names of the two teams (could be FC Brightmoor and Tall Oak Rovers), the score (2-1), minutes played (42), and which half (1st). We also want a progress bar that illustrates how many moves you have used ranging from 0-5. The scoreboard could be inspired from the ones seen around stadiums across the world, but feel free to improvise.

What We Are Looking for
We are looking for full PSD and AI files so we can use them to make minor changes like colors on shirts and shorts, colors on pitch, etc. We really want you to be innovative and inspire us, as we are not designers ourselves. In the attached files, we have tried to sketch out a design that covers our initial ideas. We are looking for a professional look, and having the players and field look like a real board game would just be awesome. A combination of the look from the realistic pitch with advertising banners around it, the idea of our spring-players and the initial thoughts of a design illustrated in our sketch, should help you along. Flat design, cartoonish or somewhere in between is up to you, we just want you to impress and make "wow"-feeling.

QUESTION:
The final screen should display a question with four possible answers. There should be a green/checkmark when correct answer, and a red/cross if incorrect.

That's all. We are looking very much forward to see your designs!
Updates

Hi all,

We have changed the terms of the contest to now have a guaranteed payment, and we are really looking forward to see your designs! Good luck.

/ Mikkel and Anders

By request we have now uploaded an AI-file with the logo for you to play around with. We are looking forward to see your designs.

/ Mikkel and Anders

Reason: Hi designers, We are really happy with the progress being made, and are looking forward to see some of the designs that are still work in progress. However the amount of designs received, has not reached our expectations yet. Therefore we are extending the deadline for seven more days, so designers, that are still working on their designs can continue their work without a stressing deadline in the horizon. Good luck to all of you. We are looking very much forward to see, what you are able to produce. Best regards, Mikkel and Anders

Reason: Hi all, We still have a lot of designers in the competition , who are battling to finish their designs, therefore we have decided to extend the deadline once more. Good luck to all of you!

Target Market(s)

Football (soccer) fans

Industry/Entity Type

Advertising

```html
<!DOCTYPE html>
<html lang="en">
<head>
<meta charset="utf-8">
<title>Quizpitch – Register</title>
<link rel="stylesheet" href="https://fonts.googleapis.com/css2?family=Inter:wght@200&family=Figtree:wght@400&family=Source+Sans+3:wght@700&display=swap">
<style>
  :root {
    --page-bg: #060d14;
    --page-glow: #0d2230;
    --screen-bg: #0a141d;
    --scene-tone-a: #1c2e3c;
    --scene-tone-b: #0b1620;
    --field-bg: rgba(170, 180, 188, 0.62);
    --field-text: #f4f6f8;
    --accent: #19b6dc;
    --accent-dark: #0e8fb3;
    --badge-ring: #0a141c;
    --tick: #e9f4f7;
    --social-top: #5a75ad;
    --social-bottom: #3c5592;
    --social-edge: #2c427a;
    --white: #ffffff;
  }
  * { margin: 0; padding: 0; box-sizing: border-box; }
  html, body { width: 1000px; height: 1200px; overflow: hidden; }
  body {
    position: relative;
    background: radial-gradient(ellipse 60% 45% at 50% 8%, var(--page-glow), var(--page-bg) 70%);
    font-family: "Figtree", sans-serif;
  }
  .app-screen {
    position: absolute;
    left: 260px; top: 162px;
    width: 480px; height: 854px;
    background: var(--screen-bg);
    overflow: hidden;
  }
  .hero-scene {
    position: absolute;
    left: 40px; top: 170px;
    width: 400px; height: 480px;
    background: radial-gradient(ellipse 55% 50% at 50% 45%, var(--scene-tone-a), var(--scene-tone-b) 75%, transparent 100%);
    opacity: 0.85;
  }
  .brand-name {
    position: absolute;
    left: 0; top: 136px; width: 480px;
    text-align: center;
    font-family: "Inter", sans-serif;
    font-weight: 200;
    font-size: 58px;
    letter-spacing: -2px;
    color: var(--white);
  }
  .register-form { position: absolute; left: 37px; top: 365px; }
  .input-field {
    width: 365px; height: 56px;
    margin-bottom: 12px;
    border-radius: 3px;
    background: var(--field-bg);
    color: var(--field-text);
    font-size: 17px;
    line-height: 56px;
    padding-left: 16px;
  }
  .input-field.is-secret { letter-spacing: 1px; line-height: 62px; }
  .valid-badge {
    position: absolute;
    left: 326px; top: 397px;
    width: 126px; height: 126px;
  }
  .social-signin {
    position: absolute;
    left: 37px; top: 731px;
    width: 405px; height: 62px;
    border-radius: 3px;
    background: linear-gradient(var(--social-top), var(--social-bottom));
    border-bottom: 5px solid var(--social-edge);
    color: var(--white);
    font-family: "Source Sans 3", sans-serif;
    font-weight: 700;
    font-size: 25px;
    line-height: 57px;
    padding-left: 108px;
  }
  .social-mark {
    position: absolute;
    left: 18px; top: 14px;
    width: 36px; height: 30px;
    background: rgba(255, 255, 255, 0.18);
  }
  .social-divider {
    position: absolute;
    left: 69px; top: 0;
    width: 2px; height: 57px;
    background: rgba(20, 35, 70, 0.45);
  }
</style>
</head>
<body>
  <main class="app-screen">
    <div class="hero-scene" role="img" aria-label="Faint photo of American football players in helmets"></div>
    <h1 class="brand-name">quizpitch</h1>

    <form class="register-form">
      <div class="input-field">alex@postmail.example</div>
      <div class="input-field is-secret">*********</div>
      <div class="input-field is-secret">*********</div>
    </form>

    <svg class="valid-badge" viewBox="0 0 126 126" aria-label="Password confirmed">
      <circle cx="63" cy="63" r="63" fill="var(--badge-ring)"/>
      <circle cx="63" cy="63" r="52" fill="var(--accent)"/>
      <path d="M63 11 a52 52 0 0 1 0 104" fill="var(--accent-dark)" opacity="0.25"/>
      <path d="M38 63 l17 17 l33 -35" fill="none" stroke="var(--tick)" stroke-width="12" stroke-linecap="square"/>
    </svg>

    <div class="social-signin">
      <span class="social-mark"></span>
      <span class="social-divider"></span>
      Sign in with Chatterly
    </div>
  </main>
</body>
</html>
```